Bed & Breakfast Wordpress Theme - Design Only

We are looking for a Wordpress theme for an award winning UK Bed & Breakfast (Guesthouse) www.fernbrookinn.co.uk
You will see that the current site is basic and dated, we need a new site that showcases the very high standard of rooms on offer and is geared towards both mobile and desktop browsing.
We would like the colours that have been used in the rooms and building (as seen on the current website) to feature in the design.
We particularly like the look of this accommodation provider website: http://www.marlowdenbarns.co.uk
Selected website images can be downloaded here, feel free to use more from the existing website too:
https://www.filevaultly.com/s/qz81mv4rt7kw0pn/website%20images.zip
Target Market(s)
The accommodation is upmarket and the design needs to subtly communicate this.
The accommodation attracts a varied mix of ages so needs to be up scale without being overly modern.
Industry/Entity Type
Accommodation
Requirements
Must have
- As the accommodation does not have a logo we need a basic typographic logo incorporated into the design.
Colours of the building and rooms must be integrated into the design in some way.
A bold homepage that allows images of the rooms on offer and key information to be visibale above the fold. The goal of the homepage is for someone to then click Rooms or Prices so calls to action may help here.
Separate designs for a sidebar and full width version of sub pages.
An area that shows off the awards won by the company on all pages and space for testimonials.
The site must enable an easy transition from - homepage - to rooms - to prices with possible call to action buttons in the top right corner on these pages
The site needs to have a Homepage layout, a general sub page layout, and a 'Rooms' page layout which will showcase all rooms available possibly in a grid layout.
Nice to have
- Please use some of the images available currently on the website in your mockup, particularly of the building and rooms.
Should not have
- No need for any type of booking fields or engine as the booking system will be embedded on a full width page.

```html
<!DOCTYPE html>
<html lang="en">
<head>
<meta charset="utf-8">
<title>Fernbrook Inn – A small and friendly hotel</title>
<link href="https://fonts.googleapis.com/css2?family=Parisienne&family=PT+Serif:wght@400;700&family=Arimo:wght@400&display=swap" rel="stylesheet">
<style>
  :root {
    --page: #eeeeec;
    --panel: #ffffff;
    --brown: #a9673a;
    --gold: #c29a62;
    --gold-soft: #d0a877;
    --tile: #f4ebdc;
    --tile-edge: #ebdcc5;
    --text: #6f6f6f;
    --muted: #8a8a8a;
    --rule: #dddddd;
    --social: #c9c3ba;
  }
  * { box-sizing: border-box; margin: 0; padding: 0; }
  html, body { width: 942px; height: 1200px; overflow: hidden; }
  body { background: var(--page); position: relative; font-family: "PT Serif", Georgia, serif; color: var(--text); }
  .abs { position: absolute; }

  .brand { left: 60px; top: 36px; font-family: "Parisienne", cursive; font-size: 44px; color: var(--brown); }

  .social { left: 677px; top: 31px; display: flex; gap: 14px; }
  .social span { width: 46px; height: 46px; border-radius: 50%; background: var(--social); display: block; }

  .main-nav { right: 39px; top: 103px; display: flex; gap: 17px; font-family: "Parisienne", cursive; font-size: 20px; color: var(--brown); }

  .panel { background: var(--panel); }
  .hero { left: 20px; top: 137px; width: 898px; height: 505px; }
  .hero-photo { left: 14px; top: 14px; width: 869px; height: 338px;
    background: linear-gradient(100deg, #e9e6dc 0%, #cdbd9f 30%, #a57d4f 55%, #8a6b45 75%, #b79466 100%); }
  .dots { right: 33px; top: 324px; display: flex; gap: 6px; }
  .dots span { width: 14px; height: 14px; border-radius: 50%; background: rgba(255,255,255,.75); }
  .dots span:first-child { background: #fff; }
  .tagline { left: 0; width: 100%; top: 370px; text-align: center; font-family: "Parisienne", cursive; font-size: 30px; color: var(--gold); }
  .intro { left: 90px; width: 718px; top: 420px; text-align: center; font-size: 13.5px; line-height: 17px; color: var(--text); }
  .book { left: 390px; top: 459px; width: 121px; height: 31px; border-radius: 8px; background: #e5e5e5; color: #777; font-size: 14px; text-align: center; line-height: 31px; }
  .arrows { top: 466px; }

  .video-card { left: 20px; top: 658px; width: 467px; height: 327px; }
  .player { left: 9px; top: 8px; width: 468px; height: 253px; background: #000; overflow: hidden; }
  .player-scene { left: 121px; top: 30px; width: 217px; height: 200px; background: linear-gradient(170deg, #e6eef0 0%, #7c9a5e 45%, #3e5a2c 100%); }
  .player-title { left: 11px; top: 8px; font-family: "Arimo", sans-serif; font-size: 12.5px; color: #fff; }
  .play { left: 204px; top: 108px; width: 62px; height: 44px; border-radius: 10px; background: rgba(30,30,30,.85); }
  .progress { left: 0; top: 228px; width: 100%; height: 3px; background: #444; }
  .time { left: 90px; top: 242px; font-family: "Arimo", sans-serif; font-size: 10px; color: #ccc; }
  .caption { left: 0; width: 100%; top: 282px; text-align: center; font-size: 15.5px; line-height: 19px; color: var(--muted); }

  .tile { width: 199px; height: 58px; background: var(--tile); border: 3px solid var(--tile-edge);
    font-weight: 700; font-size: 15.5px; color: var(--gold-soft); display: flex; align-items: center; justify-content: center; text-transform: uppercase; white-space: nowrap; letter-spacing: .1px; }

  .footer { left: 20px; top: 1007px; width: 898px; height: 167px; font-family: "Arimo", sans-serif; }
  .foot-links { left: 21px; top: 17px; font-size: 12px; color: #666; }
  .copy { right: 18px; top: 17px; font-size: 12px; color: #666; }
  .foot-rule { left: 21px; top: 40px; width: 857px; height: 1px; background: var(--rule); }
  .badge { background: #e9e2d6; }
  .address { right: 18px; top: 59px; text-align: right; font-size: 10.5px; line-height: 13px; color: #888; }
  .phone { right: 18px; top: 90px; display: flex; align-items: center; gap: 6px; font-size: 20px; font-weight: 400; color: var(--gold-soft); }
  .email { right: 18px; top: 120px; font-size: 12px; color: var(--gold-soft); }
</style>
</head>
<body>

<header>
  <div class="abs brand">Fernbrook Inn</div>
  <div class="abs social" aria-label="Social links"><span></span><span></span><span></span><span></span></div>
  <nav class="abs main-nav">
    <span>Home</span><span>Rooms</span><span>Prices</span><span>Picture Gallery</span><span>Information</span><span>Sitemap</span>
  </nav>
</header>

<section class="abs panel hero">
  <div class="abs hero-photo" role="img" aria-label="Guest bedroom with oak four-poster bed, white linen and warm bedside lamps"></div>
  <div class="abs dots"><span></span><span></span><span></span><span></span><span></span></div>
  <h1 class="abs tagline" style="font-weight:400">A small and friendly hotel</h1>
  <p class="abs intro">Award-Winning, Eco Chic, Environmentally-Responsible, New Forest Accommodation offering 24 hour front desk, daily housekeeping, private bathroom for every room.</p>
  <svg class="abs arrows" style="left:360px" width="26" height="16" viewBox="0 0 26 16"><path d="M0 2 L11 8 L0 14Z M13 2 L24 8 L13 14Z" fill="#dcdcdc"/></svg>
  <div class="abs book">BOOK NOW</div>
  <svg class="abs arrows" style="left:520px" width="26" height="16" viewBox="0 0 26 16"><path d="M26 2 L15 8 L26 14Z M13 2 L2 8 L13 14Z" fill="#dcdcdc"/></svg>
</section>

<section class="abs panel video-card">
  <div class="abs player">
    <div class="abs player-scene" role="img" aria-label="Video still of sunlit woodland trees in the New Forest"></div>
    <div class="abs player-title">Fernbrook Inn New Forest B&amp;B.wmv</div>
    <svg class="abs" style="left:418px;top:7px" width="40" height="16" viewBox="0 0 40 16"><circle cx="4" cy="8" r="2" fill="#fff"/><circle cx="12" cy="3" r="2" fill="#fff"/><circle cx="12" cy="13" r="2" fill="#fff"/><path d="M4 8 L12 3 M4 8 L12 13" stroke="#fff" stroke-width="1.3"/><circle cx="32" cy="8" r="7" fill="#fff"/><rect x="31" y="7" width="2" height="5" fill="#000"/><rect x="31" y="4" width="2" height="2" fill="#000"/></svg>
    <div class="abs play"><svg width="62" height="44" viewBox="0 0 62 44"><path d="M25 14 L39 22 L25 30Z" fill="#fff"/></svg></div>
    <div class="abs progress"></div>
    <svg class="abs" style="left:2px;top:223px" width="14" height="14"><circle cx="7" cy="7" r="6" fill="#ddd"/></svg>
    <svg class="abs" style="left:20px;top:242px" width="60" height="14" viewBox="0 0 60 14"><path d="M2 1 L14 7 L2 13Z" fill="#ccc"/><path d="M40 5 H43 L47 2 V12 L43 9 H40Z" fill="#ccc"/></svg>
    <div class="abs time"><span style="color:#fff">0:00</span> / 3:16</div>
    <svg class="abs" style="left:440px;top:242px" width="22" height="14" viewBox="0 0 22 14" fill="none" stroke="#ccc" stroke-width="1.5"><path d="M2 5 V2 H5 M17 2 H20 V5 M20 9 V12 H17 M5 12 H2 V9"/></svg>
  </div>
  <p class="abs caption">Fernbrook Inn New Forest Small and friendly hotel.<br>Formerly a 5 star B&amp;B</p>
</section>

<nav aria-label="Quick links">
  <div class="abs tile" style="left:504px;top:677px">Special Offers</div>
  <div class="abs tile" style="left:720px;top:677px">Gift Vouchers</div>
  <div class="abs tile" style="left:504px;top:754px">Awards</div>
  <div class="abs tile" style="left:720px;top:754px">New Forest Video</div>
  <div class="abs tile" style="left:504px;top:831px">B&amp;B Accessibility</div>
  <div class="abs tile" style="left:720px;top:831px">Welcome Video</div>
  <div class="abs tile" style="left:504px;top:908px">Our Environment</div>
  <div class="abs tile" style="left:720px;top:908px">Leave Car Home</div>
</nav>

<footer class="abs panel footer">
  <div class="abs foot-links">Home | Rooms | Tariffs | Activities | Eating &amp; Drinking | Travel | Links | Sitemap</div>
  <div class="abs copy">Fernbrook Inn © 2007 -2014</div>
  <div class="abs foot-rule"></div>
  <div class="abs badge" style="left:24px;top:72px;width:46px;height:74px;border-radius:6px"></div>
  <div class="abs badge" style="left:98px;top:72px;width:72px;height:72px;border-radius:50%"></div>
  <div class="abs badge" style="left:197px;top:72px;width:212px;height:76px;border-radius:6px"></div>
  <div class="abs address">Fernbrook Inn, Heath Lane,<br>Ashcombe, Hampshire SO99 4QT</div>
  <div class="abs phone">
    <svg width="22" height="22" viewBox="0 0 22 22" fill="none" stroke="currentColor" stroke-width="1.6"><circle cx="11" cy="11" r="9.5"/><path d="M8 6 C7 7 6.5 9 8.5 12 C10.5 15 12.5 16 14 15.5 L15 14 L13 12.5 L12 13.3 C11 12.7 9.8 11.4 9.2 10.2 L10 9.2 L8.8 6.8Z" fill="currentColor" stroke="none"/></svg>
    <span>01632 960418</span>
  </div>
  <div class="abs email">inquiries@fernbrookinn.co.uk</div>
</footer>

</body>
</html>
```